Corvale Real Estate

I manage 2 firms. The first one is Felmont and the logo is in blue (see the file) but i need a design for my business card for the second firm called CORVALE IMMOBILIER. This one is in charge of Real estate developer.

Colors
3176b5

```html
<!DOCTYPE html>
<html lang="en">
<head>
<meta charset="utf-8">
<title>Corvale Immobilier – Business Card</title>
<link href="https://fonts.googleapis.com/css2?family=Work+Sans:wght@400;500;600&display=swap" rel="stylesheet">
<style>
  :root {
    --backdrop: #1b1b1b;
    --card: #262626;
    --card-edge: #303030;
    --brand-blue: #3176b5;
    --silver: #a9a9a9;
    --ink-light: #f2f2f2;
    --muted: #cfcfcf;
  }
  * { margin: 0; padding: 0; box-sizing: border-box; }
  html, body {
    width: 1200px; height: 900px; overflow: hidden;
    background: var(--backdrop);
    font-family: "Work Sans", Arial, sans-serif;
  }
  .sheet {
    position: relative; width: 1200px; height: 900px;
    display: flex; flex-direction: column; align-items: center; justify-content: center; gap: 44px;
  }
  .card {
    position: relative; width: 630px; height: 360px;
    background: var(--card);
    border: 1px solid var(--card-edge);
    overflow: hidden;
  }
  /* Front */
  .card--front { display: flex; align-items: center; justify-content: center; }
  .wordmark { display: flex; align-items: center; gap: 18px; color: var(--silver); font-weight: 600; }
  .wordmark__dot { width: 54px; height: 54px; border-radius: 50%; background: var(--silver); }
  .wordmark__text { line-height: 1; }
  .wordmark__name { font-size: 44px; letter-spacing: 3px; display: block; }
  .wordmark__sub { font-size: 16px; letter-spacing: 9px; display: block; margin-top: 6px; }
  /* Back */
  .card--back { padding: 34px 0 0 40px; }
  .back-mark { color: var(--brand-blue); font-weight: 600; line-height: 1; }
  .back-mark .wordmark__name { font-size: 40px; letter-spacing: 2px; }
  .back-mark .wordmark__sub { font-size: 17px; letter-spacing: 10px; margin-top: 4px; }
  .person { margin-top: 30px; }
  .person__name { color: var(--brand-blue); font-size: 25px; font-weight: 500; letter-spacing: 1px; }
  .person__role { color: var(--ink-light); font-size: 15px; margin-top: 2px; }
  .address { color: var(--ink-light); font-size: 15px; line-height: 1.4; margin-top: 14px; }
  .contacts { list-style: none; margin-top: 12px; color: var(--ink-light); font-size: 15px; line-height: 1.55; }
  .contacts li { display: flex; align-items: center; gap: 9px; }
  .contacts svg { width: 12px; height: 12px; flex: none; }
  .back-emblem {
    position: absolute; right: 48px; top: 70px; width: 220px; height: 220px; border-radius: 50%;
    background: linear-gradient(135deg, #1f1f1f 0%, #6a6a6a 55%, #d9d9d9 100%);
  }
</style>
</head>
<body>
<main class="sheet">
  <section class="card card--front" aria-label="Card front">
    <div class="wordmark">
      <span class="wordmark__dot"></span>
      <span class="wordmark__text">
        <span class="wordmark__name">CORVALE</span>
        <span class="wordmark__sub">IMMOBILIER</span>
      </span>
    </div>
  </section>

  <section class="card card--back" aria-label="Card back">
    <div class="back-mark">
      <span class="wordmark__name">CORVALE</span>
      <span class="wordmark__sub">IMMOBILIER</span>
    </div>
    <div class="person">
      <p class="person__name">DANIEL ROCHE</p>
      <p class="person__role">Founder</p>
    </div>
    <p class="address">418 N. Harlan Avenue #205<br>Plano, TX&nbsp;&nbsp;75074</p>
    <ul class="contacts">
      <li>
        <svg viewBox="0 0 12 12" fill="var(--brand-blue)"><path d="M3 1l2 2.5-1.2 1.2a7 7 0 003.5 3.5L8.5 7 11 9l-1 2C5 11 1 7 1 2z"/></svg>
        469-555-0187
      </li>
      <li>
        <svg viewBox="0 0 12 12" fill="none" stroke="var(--brand-blue)" stroke-width="1.2"><rect x="1" y="2.5" width="10" height="7"/><path d="M1 2.5l5 4 5-4"/></svg>
        hello@corvaleimmo.com
      </li>
      <li>
        <svg viewBox="0 0 12 12" fill="none" stroke="var(--brand-blue)" stroke-width="1.1"><circle cx="6" cy="6" r="5"/><ellipse cx="6" cy="6" rx="2.2" ry="5"/><path d="M1 6h10"/></svg>
        corvaleimmobilier.com
      </li>
    </ul>
    <div class="back-emblem" aria-hidden="true"></div>
  </section>
</main>
</body>
</html>
```